Marks of Dunmore business card design

I need a clean, professional looking design using the attached logo with a bright green/ gray/dark gray/black colors. Maybe even an orange accent if it looks good. I am open to slight changes in the logo if needed. Details below on the info on what should be on the cards. We are a sign company in Ft. Lauderdale FL that specializes in yacht lettering on multi million dollar yachts.

Target Market(s)

marine industry, yachts

Industry/Entity Type

Business

Colors
9bcb3c
000000
606060
f37122

Requirements
Must have
• address: 2847 W. Harlow Rd.
• Larkhaven, OR 33417
• Phone: 555-518-3046
• email/website: marksofdunmore@mailvista.net MarksofDunmore.net
Nice to have
• I would like it very clean and simple but professional looking. Nice layout and would prefer a darker background. Orange highlight only if it works.
Should not have
• Nothing fancy.

```html
<!DOCTYPE html>
<html lang="en">
<head>
<meta charset="utf-8">
<title>Marks of Dunmore – Business Card</title>
<link rel="stylesheet" href="https://fonts.googleapis.com/css2?family=Roboto:wght@400;500;900&display=swap">
<style>
  :root {
    --backdrop: #5c5c5c;
    --card: #1b1b1b;
    --green: #14a03c;
    --gray: #8a8a8a;
    --light: #d8d8d8;
  }
  * { box-sizing: border-box; margin: 0; padding: 0; }
  html, body {
    width: 1200px;
    height: 828px;
    overflow: hidden;
    background: var(--backdrop);
    font-family: "Roboto", Arial, sans-serif;
  }
  .stage {
    width: 1200px;
    height: 828px;
    display: flex;
    align-items: center;
    justify-content: center;
  }
  .business-card {
    width: 840px;
    height: 480px;
    background: var(--card);
    box-shadow: 0 18px 40px rgba(0,0,0,0.45);
    display: flex;
    flex-direction: column;
    align-items: center;
    padding-top: 110px;
    text-align: center;
  }
  .brand-name {
    color: var(--green);
    font-weight: 900;
    font-size: 66px;
    letter-spacing: 1px;
    text-transform: uppercase;
    line-height: 1;
  }
  .holder-name {
    margin-top: 40px;
    color: var(--green);
    font-weight: 900;
    font-size: 34px;
    letter-spacing: 0.5px;
    text-transform: uppercase;
    line-height: 1;
  }
  .holder-title {
    margin-top: 6px;
    color: var(--gray);
    font-weight: 500;
    font-size: 24px;
    text-transform: uppercase;
    line-height: 1;
  }
  .address {
    margin-top: 44px;
    color: var(--light);
    font-size: 19px;
    letter-spacing: 0.5px;
  }
  .contact-row {
    margin-top: 8px;
    display: flex;
    gap: 16px;
    color: var(--light);
    font-size: 19px;
    letter-spacing: 0.5px;
  }
  .contact-item {
    display: flex;
    align-items: center;
    gap: 6px;
  }
  .contact-item svg {
    width: 14px;
    height: 14px;
    fill: var(--green);
  }
</style>
</head>
<body>
<main class="stage">
  <section class="business-card">
    <div class="brand-name">Marks of Dunmore</div>
    <div class="holder-name">Dale Corwin</div>
    <div class="holder-title">CEO/Founder</div>
    <div class="address">2847 W. Harlow Rd., Larkhaven, OR 33417</div>
    <div class="contact-row">
      <span class="contact-item">
        <svg viewBox="0 0 24 24" aria-hidden="true"><path d="M6.6 10.8a15.1 15.1 0 0 0 6.6 6.6l2.2-2.2c.3-.3.7-.4 1-.2 1.1.4 2.3.6 3.6.6.6 0 1 .4 1 1V20c0 .6-.4 1-1 1A17 17 0 0 1 3 4c0-.6.4-1 1-1h3.5c.6 0 1 .4 1 1 0 1.3.2 2.5.6 3.6.1.3 0 .7-.2 1z"/></svg>
        555-518-3046
      </span>
      <span class="contact-item">
        <svg viewBox="0 0 24 24" aria-hidden="true"><path d="M2 5h20v14H2z"/></svg>
        marksofdunmore@mailvista.net
      </span>
      <span class="contact-item">
        <svg viewBox="0 0 24 24" aria-hidden="true"><circle cx="12" cy="12" r="10"/></svg>
        MarksofDunmore.net
      </span>
    </div>
  </section>
</main>
</body>
</html>
```